Tembo & Lusani Advocates website

An interactive professional law firm website fully synchronized with social media pages.

Target Market(s)

Corporations and professionals

Industry/Entity Type

Professional Service

Number of Pages Required

5+ page

Font styles to use
Sans Serif

Colors

Designer to choose colors to be used in the design.

```html
<!DOCTYPE html>
<html lang="en">
<head>
<meta charset="utf-8">
<title>Tembo &amp; Lusani Advocates</title>
<link rel="stylesheet" href="https://fonts.googleapis.com/css2?family=Montserrat:wght@400;500;600;700&family=Lato:wght@400;700&family=Cormorant+Garamond:wght@500&display=swap">
<style>
:root{
  --red:#8f1a25;
  --red-dark:#7a131d;
  --ink:#2b2b2b;
  --muted:#555;
  --white:#fff;
  --light:#f4f4f4;
  --footer:#1e1e1e;
  --rule:#dcdcdc;
}
*{margin:0;padding:0;box-sizing:border-box}
html,body{width:1200px;height:4800px;overflow:hidden}
body{font-family:"Lato",sans-serif;color:var(--ink);background:var(--white);position:relative}
.abs{position:absolute}
.brand{display:flex;align-items:center;gap:16px}
.brand-square{width:58px;height:58px;background:var(--red)}
.brand-name{font-family:"Cormorant Garamond",serif;font-size:34px;line-height:1.05;color:var(--red)}
.brand-tag{font-family:"Montserrat",sans-serif;font-size:9px;letter-spacing:3px;color:var(--red);margin-top:8px}

/* header */
.site-header{top:0;left:0;width:1200px;height:154px}
.site-header .brand{position:absolute;left:96px;top:38px}
.header-call{position:absolute;left:660px;top:72px;text-align:center;width:160px}
.header-call small,.header-follow small{display:block;font-family:"Montserrat",sans-serif;font-size:15px;font-weight:600;color:var(--ink)}
.header-call strong{display:block;font-family:"Montserrat",sans-serif;font-size:21px;color:var(--red);margin-top:10px}
.header-follow{position:absolute;left:930px;top:72px;width:140px;text-align:center}
.social{display:flex;gap:12px;justify-content:center;margin-top:14px}
.social span{width:16px;height:16px;border-radius:50%;background:var(--red)}
.main-nav{top:154px;left:0;width:1200px;height:32px;background:var(--red);display:flex;align-items:center;padding-left:90px;gap:0}
.main-nav a{font-family:"Montserrat",sans-serif;font-size:15px;font-weight:500;color:var(--white);text-decoration:none;padding:0 29px;line-height:32px}
.main-nav a.active{background:#d9d9d9;color:var(--ink)}

/* hero */
.hero{top:186px;left:0;width:1200px;height:662px;background:linear-gradient(180deg,#cfd7e0 0%,#e6ebf0 40%,#b7c1cb 75%,#9aa4ae 100%)}
.hero .brand{position:absolute;left:150px;top:118px}
.hero-copy{position:absolute;left:130px;top:230px;width:400px;font-size:14px;line-height:1.4;color:#3a3a3a}
.btn{display:inline-block;background:var(--red);color:var(--white);font-family:"Montserrat",sans-serif;font-weight:600;font-size:15px;text-align:center;line-height:40px;height:40px}
.hero .btn{position:absolute;left:232px;top:334px;width:206px}

/* section titles */
.sec-title{font-family:"Montserrat",sans-serif;font-weight:400;font-size:29px;text-align:center;width:1200px;left:0}
.sec-rule{left:475px;width:250px;height:1px;background:var(--rule)}

/* about */
.about-photo{left:90px;top:1008px;width:1020px;height:432px;background:linear-gradient(180deg,#6d7077 0%,#3c3f46 55%,#25272c 100%)}
.about-copy{left:90px;top:1470px;width:1020px;font-size:13.5px;line-height:1.45;color:var(--muted);text-align:center}
.about-copy p{margin-bottom:14px}

/* how we do it */
.how{top:1690px;left:0;width:1200px;height:492px;background:var(--red);color:var(--white)}
.how .sec-title{top:60px;color:var(--white)}
.how .sec-rule{top:118px;background:rgba(255,255,255,.35)}
.values{position:absolute;top:188px;left:210px;width:780px;display:flex;justify-content:space-between}
.value{width:240px;text-align:center}
.value svg{width:52px;height:52px;display:block;margin:0 auto}
.value h3{font-family:"Montserrat",sans-serif;font-weight:600;font-size:17px;margin:14px 0 14px}
.value p{font-size:13px;line-height:1.4;color:#f1dcdd}

/* practice */
.practice{top:2182px;left:0;width:1200px;height:810px;background:linear-gradient(90deg,#f2f2f2,#ffffff 40%,#e9e9ea)}
.practice .sec-title{top:80px}
.practice .sec-rule{top:138px}
.cards{position:absolute;top:202px;left:141px;width:956px;display:flex;justify-content:space-between}
.card{width:310px;text-align:center}
.card-img{height:176px;border:1px solid #cfcfcf}
.card h3{font-family:"Montserrat",sans-serif;font-weight:600;font-size:17px;color:var(--red);margin:26px 0 12px}
.card p{font-size:13px;line-height:1.42;color:var(--muted);padding:0 22px;height:200px}
.card .btn{width:144px;height:36px;line-height:36px;font-size:14px;margin-top:14px}

/* professionals */
.team{top:2992px;left:0;width:1200px;height:640px;background:var(--red);color:var(--white)}
.team .sec-title{top:60px;color:var(--white)}
.team .sec-rule{top:118px;background:rgba(255,255,255,.35)}
.people{position:absolute;top:204px;left:75px;width:1050px;display:flex}
.person{width:210px;text-align:center}
.portrait{width:188px;height:188px;border-radius:50%;margin:0 auto;border:4px solid #fff;background:radial-gradient(circle at 50% 40%,#5aa9c9 0%,#2f6f8f 60%,#1d3f55 100%)}
.person h4{font-family:"Montserrat",sans-serif;font-weight:600;font-size:15px;margin-top:20px}
.person p{font-size:13px;margin-top:4px;line-height:1.3;color:#f1dcdd}
.team .btn{position:absolute;left:525px;top:510px;width:168px;height:34px;line-height:34px;background:var(--white);color:var(--red);font-size:14px}

/* clients */
.clients{top:3632px;left:0;width:1200px;height:496px;background:var(--light)}
.clients .sec-title{top:66px}
.clients .sec-rule{top:124px}
.client-row{position:absolute;top:200px;left:110px;width:980px;display:flex;justify-content:space-between;align-items:center}
.client{display:flex;align-items:center;gap:8px;font-family:"Montserrat",sans-serif;font-weight:700;font-size:15px}
.client i{display:block;width:20px;height:20px}
.clients .btn{position:absolute;left:530px;top:364px;width:140px;height:34px;line-height:34px;font-size:14px}

/* footer */
.site-footer{top:4128px;left:0;width:1200px;height:592px;background:var(--footer);color:#cfcfcf}
.footer-photo{position:absolute;right:0;top:0;width:620px;height:592px;background:linear-gradient(90deg,var(--footer) 0%,#3a3a3a 45%,#6a6a6a 100%)}
.footer-brand{position:absolute;left:141px;top:86px;display:flex;align-items:center;gap:12px}
.footer-brand span{width:20px;height:20px;background:var(--red)}
.footer-brand strong{font-family:"Montserrat",sans-serif;font-weight:600;font-size:18px;color:var(--white)}
.f-head{font-family:"Montserrat",sans-serif;font-weight:500;font-size:17px;color:var(--red);letter-spacing:1px;border-bottom:1px solid #444;padding-bottom:8px;width:200px}
.f-links{position:absolute;left:141px;top:184px}
.f-links ul{list-style:none;margin-top:18px}
.f-links li{font-size:14px;line-height:26px;color:#ddd}
.f-links li::before{content:"\203A";color:var(--red);margin-right:8px}
.f-contact{position:absolute;left:397px;top:184px;font-size:13px;line-height:1.45}
.f-contact p{margin-top:18px;color:#ccc}
.f-contact ul{list-style:none;margin-top:12px}
.f-contact li{display:flex;align-items:center;gap:8px;line-height:20px}
.f-contact li svg{width:12px;height:12px}
.f-follow{position:absolute;left:141px;top:442px}
.f-follow .social{justify-content:flex-start;margin-top:18px;gap:6px}
.f-follow .social span{width:18px;height:18px;background:#ddd}
.f-call{position:absolute;left:397px;top:442px}
.f-call strong{display:block;font-family:"Montserrat",sans-serif;font-size:26px;color:var(--white);margin-top:18px;font-weight:500}
.legal{top:4720px;left:0;width:1200px;height:80px;background:var(--red);color:#f1dcdd;font-size:13px;padding-left:141px;line-height:80px}
</style>
</head>
<body>

<header class="abs site-header">
  <div class="brand">
    <div class="brand-square"></div>
    <div>
      <div class="brand-name">Tembo &amp; Lusani<br>Advocates</div>
      <div class="brand-tag">CONSTRUCTION LAW | ARBITRATION | LITIGATION</div>
    </div>
  </div>
  <div class="header-call"><small>Call us</small><strong>(555) 210 4378</strong></div>
  <div class="header-follow"><small>Follow us</small>
    <div class="social"><span></span><span></span><span></span><span></span></div>
  </div>
</header>

<nav class="abs main-nav">
  <a class="active">Home</a><a>About Us</a><a>Practice Areas</a><a>Our clients</a><a>Our Professionals</a><a>Contact Us</a><a>Fix Appointment</a>
</nav>

<section class="abs hero" role="img" aria-label="Long concrete bridge stretching over calm water under a pale sky">
  <div class="brand">
    <div class="brand-square"></div>
    <div>
      <div class="brand-name">Tembo &amp; Lusani<br>Advocates</div>
      <div class="brand-tag">CONSTRUCTION LAW | ARBITRATION | LITIGATION</div>
    </div>
  </div>
  <p class="hero-copy">Lorem ipsum dolor sit amet, consectetuer adipiscing elit. Aenean commodo ligula eget dolor. Aenean massa. Cum sociis natoque penatibus et magnis dis parturient montes, nascetur ridiculus mus. Donec quam felis, ultricies nec, pellentesque eu, pretium quis, sem.</p>
  <a class="btn">MAKE APPOINTMENT</a>
</section>

<h2 class="abs sec-title" style="top:908px;color:var(--red)">About Tembo Lusani Advocates</h2>
<div class="abs sec-rule" style="top:966px"></div>
<div class="abs about-photo" role="img" aria-label="Group photograph of the firm's partners and associates in business suits"></div>
<div class="abs about-copy">
  <p>In 1996, our firm was founded and is comprised of 5 Partners and over 15 Associates and support staff fully engaged and focused on client service. The firm is fully automated and is run on the latest practice management software with efficient client focused delivery systems and improved turn around times.</p>
  <p>Over the years, the firm has worked with the International firm of Harcourt Vale in successfully representing Civic Rights Forum against a multimillion dollar law suit and has acted for both local and international corporations from China, Italy, Turkey, South Africa, Zambia and the United Kingdom to build their businesses.</p>
  <p>With over 17 years' experience and having achieved tremendous success for our clients having won over 200 commercial disputes, we are now a specialist firm in Commercial Litigation, Construction Law and Arbitration. We have successfully represented clients in ground breaking cases in the financial services sector that we are the firm of choice in banking and insurance litigation.</p>
</div>

<section class="abs how">
  <h2 class="abs sec-title">How we do it</h2>
  <div class="abs sec-rule"></div>
  <div class="values">
    <div class="value">
      <svg viewBox="0 0 52 52" fill="none" stroke="#fff" stroke-width="3"><path d="M26 4 L44 11 V26 C44 37 36 45 26 48 C16 45 8 37 8 26 V11 Z"/><path d="M18 27 L24 33 L35 20"/></svg>
      <h3>Integrity</h3>
      <p>We maintain ethical behaviour and strict moral values. We are honest and trustworthy in our dealings with each other, with our clients and with all others with whom we deal.</p>
    </div>
    <div class="value">
      <svg viewBox="0 0 52 52" fill="none" stroke="#fff" stroke-width="3" stroke-linejoin="round"><path d="M3 22 L14 14 L24 20 L30 16 L49 22"/><path d="M14 14 L6 30 L20 42 L28 44 L44 32 L49 22"/><path d="M24 20 L18 28 L28 30 L36 26"/></svg>
      <h3>Partnership</h3>
      <p>We partner with our clients and keep a close and interactive relationship that enriches our business knowledge and allows us to provide strategic, innovative and forward thinking solutions fit to meet the challenges they face every day.</p>
    </div>
    <div class="value">
      <svg viewBox="0 0 52 52" fill="none" stroke="#fff" stroke-width="3"><circle cx="26" cy="26" r="9"/><path d="M26 4 V11 M26 41 V48 M4 26 H11 M41 26 H48 M10 10 L15 15 M37 37 L42 42 M42 10 L37 15 M15 37 L10 42"/></svg>
      <h3>Efficiency</h3>
      <p>We work to surpass our clients' expectations. We are practical and solution driven in our approach. We are innovative and creative, and we focus sharply and firmly on the issues we undertake.</p>
    </div>
  </div>
</section>

<section class="abs practice">
  <h2 class="abs sec-title" style="color:var(--red)">Practice Areas</h2>
  <div class="abs sec-rule"></div>
  <div class="cards">
    <article class="card">
      <div class="card-img" role="img" aria-label="Steel roof structure of a building under construction" style="background:linear-gradient(160deg,#9fc3da,#4f7590 60%,#2f4a5e)"></div>
      <h3>Construction Law</h3>
      <p>Our Construction Law department is headed by our Senior Partner who is highly qualified and experienced in Construction law and in providing advice on contract management under the FIDIC, JCT, NEC and ICE forms of contracts. We advise on all aspects of claim procedures as well as claim preparation and enforcement (or defence) strategies; advice on assessment and formulation.</p>
      <a class="btn">READ MORE</a>
    </article>
    <article class="card">
      <div class="card-img" role="img" aria-label="Hands signing a commercial contract on a desk" style="background:linear-gradient(160deg,#f3f3f1,#d9d6cf 60%,#b8b3a8)"></div>
      <h3>Commercial Litigation</h3>
      <p>We have a reputation for producing excellent results for our litigation clients. Since 1996, the firm has an excellent track record of winning for our clients in commercial disputes. The firm has built effective litigation teams that actively involve all advocates; this teamwork ensures formulation of accurate legal strategies and excellent results at all stages.</p>
      <a class="btn">READ MORE</a>
    </article>
    <article class="card">
      <div class="card-img" role="img" aria-label="Judge's gavel resting on an arbitration agreement" style="background:linear-gradient(160deg,#8b8b8b,#4c4c4c 60%,#2a2a2a)"></div>
      <h3>Arbitration</h3>
      <p>We advise clients on both domestic and international arbitration proceedings and other forms of intermediate and alternative dispute resolution, as well as on contract management of claims arising during the course of a project. Our team helps clients weigh the merits of litigating against using arbitration or other types of ADR procedures.</p>
      <a class="btn">READ MORE</a>
    </article>
  </div>
</section>

<section class="abs team">
  <h2 class="abs sec-title">Our Professionals</h2>
  <div class="abs sec-rule"></div>
  <div class="people">
    <div class="person"><div class="portrait" role="img" aria-label="Portrait of the Managing Partner"></div><h4>JOHN.K.TEMBO</h4><p>Managing Partner</p></div>
    <div class="person"><div class="portrait" role="img" aria-label="Portrait of the Senior Partner"></div><h4>DAVID.S.LUSANI</h4><p>Senior Partner</p></div>
    <div class="person"><div class="portrait" role="img" aria-label="Portrait of the Head of Litigation"></div><h4>SAM OKELLO</h4><p>Partner (Head of Litigation)</p></div>
    <div class="person"><div class="portrait" role="img" aria-label="Portrait of the Head of Business Developments"></div><h4>NICHOLAS MWENDA</h4><p>Partner (Head of<br>Business Developments)</p></div>
    <div class="person"><div class="portrait" role="img" aria-label="Portrait of the Head of Corporate Advisory"></div><h4>SHEILA NANSUBUGA</h4><p>Partner (Head of<br>Corporate Advisory)</p></div>
  </div>
  <a class="btn">FIX APPOINTMENT</a>
</section>

<section class="abs clients">
  <h2 class="abs sec-title" style="color:var(--red)">Practice Areas</h2>
  <div class="abs sec-rule"></div>
  <div class="client-row">
    <div class="client" style="color:#c8102e"><i style="background:#f2c200"></i>Swiftline</div>
    <div class="client" style="color:#3a3a3a">Savanna Foods</div>
    <div class="client" style="color:#c8102e"><i style="background:#c8102e"></i>Crestmark</div>
    <div class="client" style="color:#2a4a8a">Unity Assure</div>
    <div class="client" style="color:#1f4f8f">Boxwell</div>
    <div class="client" style="color:#2f8fb0">Roadhire</div>
    <div class="client" style="color:#3b8c3b"><i style="background:#3b8c3b;border-radius:50%"></i>Verdant</div>
  </div>
  <a class="btn">READ MORE</a>
</section>

<footer class="abs site-footer">
  <div class="footer-photo" role="img" aria-label="Faded classical stone columns of a courthouse"></div>
  <div class="footer-brand"><span></span><strong>Tembo &amp; Lusani</strong></div>
  <div class="f-links">
    <div class="f-head">QUICK LINKS</div>
    <ul><li>About Us</li><li>Practice Areas</li><li>Our clients</li><li>Our Professionals</li><li>Contact Us</li></ul>
  </div>
  <div class="f-contact">
    <div class="f-head">CONTACT</div>
    <p>Head Office Address &amp; Contacts<br>Plot 18 Riverside Avenue<br>3rd Floor, Lake House<br>P. O Box 5024<br>Easton</p>
    <ul>
      <li><svg viewBox="0 0 12 12"><path d="M2 1 L4.5 1 L5.5 4 L4 5 C4.8 6.8 5.5 7.5 7 8 L8 6.5 L11 7.5 V10 C6 11 1 6 2 1Z" fill="#b33"/></svg>0555 218 641</li>
      <li><svg viewBox="0 0 12 12"><path d="M2 1 L4.5 1 L5.5 4 L4 5 C4.8 6.8 5.5 7.5 7 8 L8 6.5 L11 7.5 V10 C6 11 1 6 2 1Z" fill="#b33"/></svg>+000 (0) 555 218 642</li>
      <li><svg viewBox="0 0 12 12"><rect x="1" y="3" width="10" height="7" fill="none" stroke="#b33"/><path d="M1 3 L6 7 L11 3" fill="none" stroke="#b33"/></svg>advocates@tembolaw.example</li>
      <li><svg viewBox="0 0 12 12"><circle cx="6" cy="6" r="4.5" fill="none" stroke="#b33"/></svg>www.tembolaw.example</li>
    </ul>
  </div>
  <div class="f-follow">
    <div class="f-head">FOLLOW US ON</div>
    <div class="social"><span></span><span></span><span></span><span></span><span></span></div>
  </div>
  <div class="f-call">
    <div class="f-head">CALL US ON</div>
    <strong>0555 218 640</strong>
  </div>
</footer>

<div class="abs legal">© 2017 tembolaw &nbsp;|&nbsp; Privacy Policy &nbsp;|&nbsp; User Agreement</div>

</body>
</html>
```